Website creation for audiovisual activities

I want a website for my director of photography activity. It's primarily composed of screenshots in gallery format, followed by detailed pages for each production.

Here's my current website:
www.lumavexstudio.com
I'd like a more modern and streamlined design, and for the site to be responsive on phones and computers. I also want to be able to easily add photos and text to it later.

Target Market(s)

productions society, directors and producers.

Industry/Entity Type

Audiovisual / TV

Coding

Coded - Design and coding required

Number of Pages Required

5+ page

Font styles to use
Sans Serif

Colors
0054AA
0677BA
7BADD7
CADEEF
E8F1F8
0094D4
00A9DD
6FCCEA
C7EBF8
E9F6FB
00AB8E
00BBA5
67D7C9
C6EFE9
E9F9F6
6B429C
8869AF
B7A5CE
E3DAEB
F3F0F8

Requirements
Must have
• a modern look with a photo gallery on the homepage
Nice to have
• a light background with large, dynamic images
Should not have
• a dark background and an overly classic look

```html
<!DOCTYPE html>
<html lang="en">
<head>
<meta charset="utf-8">
<title>Elian Vautrin — Contact</title>
<link rel="stylesheet" href="https://fonts.googleapis.com/css2?family=Inter:wght@300;400;500&display=swap">
<style>
  :root {
    --blue: #0054AA;
    --ink: #1a1a1a;
    --muted: #6b6b6b;
    --field: #f7f7f7;
    --line: #ececec;
    --note-bg: #E8F1F8;
    --page: #ffffff;
  }
  * { margin: 0; padding: 0; box-sizing: border-box; }
  html, body { width: 1200px; height: 613px; overflow: hidden; background: var(--page); }
  body { font-family: "Inter", sans-serif; color: var(--ink); position: relative; }
  .abs { position: absolute; white-space: nowrap; }

  .site-header { position: absolute; left: 0; top: 0; width: 1200px; height: 24px; border-bottom: 1px solid var(--line); }
  .brand { left: 372px; top: 6px; font-size: 8px; line-height: 12px; color: var(--blue); font-weight: 400; }
  .nav-link { top: 7px; font-size: 6.2px; line-height: 10px; color: var(--muted); }
  .nav-link.active { color: var(--blue); }
  .nav-underline { position: absolute; left: 805px; top: 23px; width: 23px; height: 1px; background: var(--blue); }

  .page-title { left: 420px; top: 56px; font-size: 19px; line-height: 26px; font-weight: 300; }
  .page-lede { left: 420px; top: 87px; font-size: 7.8px; line-height: 11px; color: var(--muted); }

  .field-label { left: 420px; font-size: 6px; line-height: 8px; font-weight: 500; }
  .field { position: absolute; left: 420px; width: 171px; background: var(--field); border-radius: 2px; }
  .send-btn { position: absolute; left: 420px; top: 310px; width: 49px; height: 14px; background: var(--blue); color: #fff; border-radius: 2px; font-size: 5.4px; font-weight: 500; display: flex; align-items: center; justify-content: center; }

  .info-title { left: 609px; top: 134px; font-size: 9.4px; line-height: 13px; font-weight: 400; }
  .info-icon { position: absolute; left: 609px; width: 7px; height: 7px; }
  .info-label { left: 623px; font-size: 6px; line-height: 8px; font-weight: 500; }
  .info-value { left: 623px; font-size: 5.3px; line-height: 7px; color: var(--muted); }
  .divider { position: absolute; left: 609px; top: 236px; width: 171px; height: 1px; background: var(--line); }

  .agent-title { left: 609px; top: 249px; font-size: 7px; line-height: 10px; font-weight: 500; }
  .agent-name { left: 609px; top: 265px; font-size: 6.2px; line-height: 9px; color: var(--muted); }
  .agent-line { left: 609px; font-size: 5.3px; line-height: 7px; color: var(--muted); }

  .availability { position: absolute; left: 609px; top: 307px; width: 171px; height: 32px; background: var(--note-bg); border-radius: 2px; padding: 9px 9px; font-size: 5.3px; line-height: 7.5px; color: var(--blue); }
</style>
</head>
<body>
  <header class="site-header">
    <span class="abs brand">Elian Vautrin</span>
    <span class="abs nav-link" style="left:711px">Work</span>
    <span class="abs nav-link" style="left:738px">About</span>
    <span class="abs nav-link" style="left:767px">Showreel</span>
    <span class="abs nav-link active" style="left:805px">Contact</span>
    <span class="nav-underline"></span>
  </header>

  <main>
    <h1 class="abs page-title">Get in Touch</h1>
    <p class="abs page-lede">Available for film, television, and commercial projects worldwide</p>

    <form>
      <label class="abs field-label" style="top:134px">Name</label>
      <div class="field" style="top:146px;height:14px"></div>
      <label class="abs field-label" style="top:169px">Email</label>
      <div class="field" style="top:180px;height:14px"></div>
      <label class="abs field-label" style="top:203px">Company / Production</label>
      <div class="field" style="top:215px;height:14px"></div>
      <label class="abs field-label" style="top:238px">Message</label>
      <div class="field" style="top:249px;height:52px"></div>
      <div class="send-btn">Send Message</div>
    </form>

    <section>
      <h2 class="abs info-title">Contact Information</h2>

      <svg class="info-icon" style="top:156px" viewBox="0 0 24 24" fill="none" stroke="#0054AA" stroke-width="2"><rect x="2" y="5" width="20" height="14" rx="2"/><path d="M2 7l10 7 10-7"/></svg>
      <span class="abs info-label" style="top:155px">Email</span>
      <span class="abs info-value" style="top:165px">contact@elianvautrin.com</span>

      <svg class="info-icon" style="top:183px" viewBox="0 0 24 24" fill="none" stroke="#0054AA" stroke-width="2"><path d="M22 16.9v3a2 2 0 0 1-2.2 2 19.8 19.8 0 0 1-8.6-3.1 19.5 19.5 0 0 1-6-6A19.8 19.8 0 0 1 2.1 4.2 2 2 0 0 1 4.1 2h3a2 2 0 0 1 2 1.7c.1 1 .4 1.9.7 2.8a2 2 0 0 1-.5 2.1L8 9.9a16 16 0 0 0 6 6l1.3-1.3a2 2 0 0 1 2.1-.4c.9.3 1.8.6 2.8.7a2 2 0 0 1 1.7 2z"/></svg>
      <span class="abs info-label" style="top:182px">Phone</span>
      <span class="abs info-value" style="top:191px">+44 20 7946 0321</span>

      <svg class="info-icon" style="top:208px" viewBox="0 0 24 24" fill="none" stroke="#0054AA" stroke-width="2"><path d="M20 10c0 6-8 12-8 12S4 16 4 10a8 8 0 0 1 16 0z"/><circle cx="12" cy="10" r="3"/></svg>
      <span class="abs info-label" style="top:207px">Location</span>
      <span class="abs info-value" style="top:216px">London, UK / Los Angeles, USA</span>

      <div class="divider"></div>

      <h3 class="abs agent-title">Agent / Representative</h3>
      <span class="abs agent-name">Northlight Agency</span>
      <span class="abs agent-line" style="top:277px">agent@northlightagency.com</span>
      <span class="abs agent-line" style="top:287px">+1 310 555 0147</span>

      <p class="availability">Currently accepting projects for Q2-Q3 2026. For urgent inquiries, please contact my agent directly.</p>
    </section>
  </main>
</body>
</html>
```